Brightmoor Crest Real Estate Company needs Website

I need an updated, easy to use website for my Real Estate company based out of Amarillo, TX.
Our current focus is on residential rental properties. However we are looking to expand into multi-family rentals, commercial rentals, and vacation rentals.
We also offer Real Estate Listing services.
The final design should be user friendly.

Target Market(s)

Homeowners and renters

Industry/Entity Type

Real Estate

Coding

Coded - Design and coding required

Number of Pages Required

1 page

Font styles to use
Sans Serif

Requirements
Must have
• Easy to navigate

```html
<!DOCTYPE html>
<html lang="en">
<head>
<meta charset="utf-8">
<title>Brightmoor Crest Real Estate Company</title>
<link href="https://fonts.googleapis.com/css2?family=Raleway:wght@400;500;600;700&family=Open+Sans:wght@400;600&display=swap" rel="stylesheet">
<style>
:root{
  --blue:#6a9ed8;
  --blue-dark:#4f86c6;
  --blue-link:#4a84c4;
  --nav-top:#86b3e3;
  --nav-bottom:#5d93d1;
  --ink:#3a3a3a;
  --muted:#6b6b6b;
  --card:#f2f2f2;
  --band:#f3f3f3;
  --line:#d9d9d9;
  --white:#ffffff;
}
*{box-sizing:border-box;margin:0;padding:0}
html,body{width:1200px;height:2757px;overflow:hidden}
body{position:relative;font-family:"Open Sans",Arial,sans-serif;color:var(--ink);background:var(--white)}
section,header,nav,footer{position:absolute;left:0;width:1200px}
.abs{position:absolute}
h2{font-family:"Raleway",Arial,sans-serif;font-weight:600;letter-spacing:.5px}

/* header */
.site-header{top:0;height:101px;background:var(--white)}
.brand{left:73px;top:30px;display:flex;align-items:center;gap:12px}
.brand-dot{width:26px;height:26px;border-radius:50%;background:var(--blue)}
.brand-name{font-family:"Raleway",sans-serif;font-weight:700;font-size:34px;color:#4a6a8e;line-height:1}
.phone{left:722px;top:40px;font-family:"Raleway",sans-serif;font-size:19px;color:#444;display:flex;align-items:center;gap:8px}
.search-box{left:913px;top:32px;width:214px;height:44px;border:1px solid #cfcfcf;background:#f6f6f6;border-radius:3px;font-size:12px;color:#555;padding:13px 12px}
.search-box svg{position:absolute;right:12px;top:11px}

/* nav */
.main-nav{top:101px;height:52px;background:linear-gradient(var(--nav-top),var(--nav-bottom));display:flex;align-items:center;padding:0 75px 0 75px;gap:0;justify-content:space-between;padding-right:80px}
.main-nav a{font-family:"Raleway",sans-serif;font-size:13px;font-weight:500;color:var(--white);text-decoration:none;text-transform:uppercase}

/* hero */
.hero{top:153px;height:509px;background:linear-gradient(180deg,#4f8fd6 0%,#8fbde8 35%,#b7d5ef 55%,#6d8fa8 72%,#4e7a3c 86%,#3c6a2c 100%)}
.hero-title{left:0;width:1200px;top:190px;text-align:center;font-family:"Raleway",sans-serif;font-weight:700;font-size:46px;line-height:64px;color:var(--white);text-shadow:0 2px 6px rgba(0,0,0,.45)}
.slider-ctrl{left:540px;top:446px}

/* property search */
.property-search{top:662px;height:202px;background:linear-gradient(#7fb0e3,#5f94d1);box-shadow:0 6px 10px rgba(0,0,0,.15)}
.property-search h2{position:absolute;top:32px;width:100%;text-align:center;color:var(--white);font-size:22px}
.field{position:absolute;height:34px;background:var(--white);border:1px solid #d5d5d5;font-size:12px;color:#555;padding:9px 12px}
.field.select::after{content:"";position:absolute;right:12px;top:10px;border:4px solid transparent;border-bottom-color:#333;border-top:0;box-shadow:none}
.field.select::before{content:"";position:absolute;right:12px;top:18px;border:4px solid transparent;border-top-color:#333;border-bottom:0}
.search-btn{position:absolute;left:834px;top:118px;width:177px;height:38px;border:2px solid var(--white);color:var(--white);font-family:"Raleway",sans-serif;font-weight:600;font-size:14px;text-align:center;line-height:34px;border-radius:3px}

/* services */
.services{top:864px;height:419px}
.services h2{position:absolute;top:58px;width:100%;text-align:center;font-size:22px;color:#444}
.service{position:absolute;top:122px;width:290px;text-align:center}
.service-icon{width:118px;height:118px;border-radius:50%;background:var(--blue);margin:0 auto;display:flex;align-items:center;justify-content:center}
.service h3{margin-top:34px;font-family:"Raleway",sans-serif;font-size:15px;font-weight:600;color:var(--blue-link);letter-spacing:.4px}
.service p{margin-top:10px;font-size:13px;line-height:24px;color:var(--muted)}

/* welcome */
.welcome{top:1283px;height:294px;background:var(--blue)}
.welcome-notch{left:572px;top:0;width:0;height:0;border-left:28px solid transparent;border-right:28px solid transparent;border-top:24px solid var(--white)}
.welcome h2{position:absolute;top:60px;width:100%;text-align:center;color:var(--white);font-size:22px}
.welcome p{position:absolute;left:79px;width:1042px;top:100px;text-align:center;color:#eef4fb;font-size:13px;line-height:27px}
.outline-btn{position:absolute;left:531px;top:213px;width:138px;height:39px;border:2px solid var(--white);color:var(--white);font-family:"Raleway",sans-serif;font-size:13px;font-weight:600;text-align:center;line-height:35px}

/* listing and sidebar */
.content{top:1577px;height:775px}
.section-title{position:absolute;font-family:"Raleway",sans-serif;font-weight:600;font-size:22px;color:#333;letter-spacing:.4px}
.view-all{left:652px;top:29px;width:116px;height:34px;border:1px solid #bbb;font-size:13px;font-weight:600;text-align:center;line-height:32px;border-radius:2px}
.listing{position:absolute;left:73px;width:693px;height:208px;background:var(--card)}
.listing-photo{position:absolute;left:24px;top:22px;width:287px;height:165px}
.listing h3{position:absolute;left:335px;top:14px;font-family:"Raleway",sans-serif;font-weight:600;font-size:17px;color:var(--blue-link)}
.listing p{position:absolute;left:335px;top:44px;width:335px;font-size:12.5px;line-height:24px;color:var(--muted)}
.price{position:absolute;left:335px;top:146px;width:167px;height:40px;border:2px solid #c9c9c9;background:var(--white);font-family:"Raleway",sans-serif;font-weight:700;font-size:22px;text-align:center;line-height:36px;color:#333}
.more-btn{position:absolute;left:517px;top:149px;width:112px;height:34px;background:var(--blue);color:var(--white);font-family:"Raleway",sans-serif;font-size:12px;font-weight:600;text-align:center;line-height:34px}

.member{position:absolute;left:794px;width:333px;height:138px}
.member-photo{position:absolute;left:0;top:0;width:121px;height:138px;background:linear-gradient(#e8e8e8,#c4c8cc)}
.member h4{position:absolute;left:147px;top:0;font-family:"Raleway",sans-serif;font-weight:600;font-size:16px;color:var(--blue-link)}
.member p{position:absolute;left:147px;top:26px;width:186px;font-size:12.5px;line-height:23px;color:var(--muted)}
.member-links{position:absolute;left:147px;top:116px;display:flex;gap:14px}
.member-links span{width:18px;height:18px;background:#5b5b5b;border-radius:3px}
.divider{position:absolute;left:794px;top:426px;width:333px;height:2px;background:var(--line)}
.blog-arrows{position:absolute;left:1076px;top:459px;display:flex;gap:6px}
.blog-arrows span{width:21px;height:21px;border-radius:50%;background:#a7a7a7;display:flex;align-items:center;justify-content:center}
.post{position:absolute;left:794px;width:333px}
.post h4{font-family:"Raleway",sans-serif;font-weight:600;font-size:16px;color:var(--blue-link)}
.post time{display:block;margin-top:6px;font-size:11px;color:#999}
.post p{margin-top:6px;font-size:12.5px;line-height:26px;color:var(--muted)}

/* press */
.press{top:2352px;height:160px;background:var(--band)}
.press h2{position:absolute;top:42px;width:100%;text-align:center;font-size:22px;color:#333}
.press-marks{position:absolute;top:88px;left:0;width:1200px;display:flex;justify-content:center;align-items:center;gap:28px}
.press-marks span{height:22px;background:#3d3d3d;border-radius:2px;opacity:.85}

/* footer */
.site-footer{top:2512px;height:245px;background:var(--blue)}
.footer-brand{left:75px;top:44px;display:flex;align-items:center;gap:10px}
.footer-brand .brand-dot{background:var(--white);width:20px;height:20px}
.footer-brand .brand-name{color:var(--white);font-size:26px}
.small-note{font-size:12px;color:#eef4fb;line-height:24px}
.footer-col h5{font-family:"Raleway",sans-serif;font-weight:600;font-size:13px;color:var(--white);letter-spacing:.4px;margin-bottom:6px}
.footer-col a,.footer-col div{display:block;color:var(--white);font-size:12px;line-height:26px;text-decoration:none}
.socials{left:910px;top:80px;display:flex;gap:7px}
.socials span{width:37px;height:37px;border:2px solid var(--white);border-radius:50%}
</style>
</head>
<body>

<header class="site-header">
  <div class="abs brand"><span class="brand-dot"></span><span class="brand-name">Brightmoor Crest</span></div>
  <div class="abs phone">
    <svg width="15" height="15" viewBox="0 0 24 24"><path fill="#555" d="M6.6 10.8a15.1 15.1 0 0 0 6.6 6.6l2.2-2.2a1 1 0 0 1 1-.25 11.4 11.4 0 0 0 3.6.57 1 1 0 0 1 1 1V20a1 1 0 0 1-1 1A17 17 0 0 1 3 4a1 1 0 0 1 1-1h3.5a1 1 0 0 1 1 1c0 1.25.2 2.45.57 3.57a1 1 0 0 1-.25 1z"/></svg>
    1-800-555-0142
  </div>
  <div class="abs search-box">Search..
    <svg width="20" height="20" viewBox="0 0 24 24"><circle cx="10" cy="10" r="6.5" fill="none" stroke="#333" stroke-width="2.6"/><path d="M15 15l6 6" stroke="#333" stroke-width="2.8" stroke-linecap="round"/></svg>
  </div>
</header>

<nav class="main-nav">
  <a href="#">Home</a><a href="#">About Us</a><a href="#">Services</a><a href="#">Property Search</a><a href="#">Blog</a><a href="#">Latest News</a><a href="#">Testimonials</a><a href="#">Careers</a><a href="#">Contact Us</a>
</nav>

<section class="hero" role="img" aria-label="City skyline of glass towers under a blue sky with green trees in front">
  <h1 class="abs hero-title">Real Estate company based out of<br>Amarillo, TX</h1>
  <svg class="abs slider-ctrl" width="130" height="30" viewBox="0 0 130 30">
    <path d="M14 4 4 15l10 11" fill="none" stroke="#fff" stroke-width="3"/>
    <circle cx="33" cy="15" r="5" fill="#fff"/><circle cx="52" cy="15" r="5" fill="none" stroke="#fff" stroke-width="2"/>
    <circle cx="71" cy="15" r="5" fill="#fff"/><circle cx="90" cy="15" r="5" fill="#fff"/>
    <path d="M112 4l10 11-10 11" fill="none" stroke="#fff" stroke-width="3"/>
  </svg>
</section>

<section class="property-search">
  <h2>PROPERTY SEARCH</h2>
  <div class="field" style="left:191px;top:77px;width:241px">Keyword Search..</div>
  <div class="field select" style="left:447px;top:77px;width:187px">No of Bedroom</div>
  <div class="field select" style="left:641px;top:77px;width:175px">No of Bathroom</div>
  <div class="field select" style="left:834px;top:77px;width:177px">Location</div>
  <div class="field" style="left:191px;top:121px;width:241px">Enter Area Sqft.</div>
  <div class="field select" style="left:447px;top:121px;width:187px">Min Price</div>
  <div class="field select" style="left:641px;top:121px;width:175px">Max Price</div>
  <div class="search-btn">SEARCH</div>
</section>

<section class="services">
  <h2>OUR SERVICES OFFER</h2>
  <div class="service" style="left:94px">
    <div class="service-icon"><svg width="56" height="56" viewBox="0 0 56 56"><path d="M6 26 28 8l22 18" fill="none" stroke="#fff" stroke-width="4"/><path d="M12 24v24h32V24" fill="none" stroke="#fff" stroke-width="4"/><circle cx="22" cy="32" r="4" fill="#fff"/><circle cx="34" cy="32" r="4" fill="#fff"/><rect x="17" y="37" width="10" height="11" fill="#fff"/><rect x="29" y="37" width="10" height="11" fill="#fff"/></svg></div>
    <h3>MULTI-FAMILY RENTALS</h3>
    <p>Duis aliquam nibh a dui iaculis viverra id a velit. Vivamus egestas risus in magna varius commodo. Sed semper viverra..</p>
  </div>
  <div class="service" style="left:454px">
    <div class="service-icon"><svg width="56" height="56" viewBox="0 0 56 56"><path d="M6 18 28 7l22 11z" fill="#fff"/><rect x="8" y="20" width="40" height="4" fill="#fff"/><rect x="12" y="26" width="5" height="16" fill="#fff"/><rect x="21" y="26" width="5" height="16" fill="#fff"/><rect x="30" y="26" width="5" height="16" fill="#fff"/><rect x="39" y="26" width="5" height="16" fill="#fff"/><rect x="6" y="44" width="44" height="5" fill="#fff"/></svg></div>
    <h3>COMMERCIAL RENTALS</h3>
    <p>Duis aliquam nibh a dui iaculis viverra id a velit. Vivamus egestas risus in magna varius commodo. Sed semper viverra..</p>
  </div>
  <div class="service" style="left:814px">
    <div class="service-icon"><svg width="56" height="56" viewBox="0 0 56 56"><path d="M34 44 38 14" stroke="#fff" stroke-width="3"/><path d="M38 14c-6-6-14-4-16 0 6-2 11-1 16 0zm0 0c5-6 13-6 15-1-6-1-10-1-15 1z" fill="#fff"/><circle cx="20" cy="32" r="4" fill="#fff"/><path d="M10 44c6-6 12-8 20-6l4 3" fill="none" stroke="#fff" stroke-width="3"/><path d="M6 48h44" stroke="#fff" stroke-width="3"/></svg></div>
    <h3>VACATION RENTALS</h3>
    <p>Duis aliquam nibh a dui iaculis viverra id a velit. Vivamus egestas risus in magna varius commodo. Sed semper viverra..</p>
  </div>
</section>

<section class="welcome">
  <div class="abs welcome-notch"></div>
  <h2>WELCOME TO BRIGHTMOOR CREST</h2>
  <p>Vestibulum vel metus sit amet turpis bibendum tincidunt vel sit amet quam. Pellentesque habitant morbi tristique senectus et netus et malesuada fames ac turpis egestas. Nunc consequat congue nulla eu imperdiet. Donec in est erat, id malesuada turpis. Nunc a dui id turpis convallis semper. Nunc dignissim lectus vitae eros placerat euismod. Aenean lacinia sodales eros, sit amet molestie enim consectetur eget.</p>
  <div class="outline-btn">READ MORE</div>
</section>

<section class="content">
  <h2 class="section-title" style="left:73px;top:32px">REAL ESTATE LISTING</h2>
  <div class="abs view-all">View All</div>

  <article class="listing" style="top:90px">
    <div class="listing-photo" role="img" aria-label="White villa with pool at dusk" style="background:linear-gradient(#3b5f8f,#c9b08a 60%,#3d6f8f)"></div>
    <h3>Nsectetur eget</h3>
    <p>Vestibulum ante ipsum primis in faucibus orci luctus et ultrices posuere. Vestibulum ante ipsum primis in faucibus orci luctus et ultrices..</p>
    <div class="price">$253,23.00</div><div class="more-btn">MORE INFO</div>
  </article>
  <article class="listing" style="top:309px">
    <div class="listing-photo" role="img" aria-label="Two-storey house with garden under blue sky" style="background:linear-gradient(#7fb2e0,#d8cfc0 55%,#4f7d3a)"></div>
    <h3>Nsectetur eget</h3>
    <p>Vestibulum ante ipsum primis in faucibus orci luctus et ultrices posuere. Vestibulum ante ipsum primis in faucibus orci luctus et ultrices..</p>
    <div class="price">$253,23.00</div><div class="more-btn">MORE INFO</div>
  </article>
  <article class="listing" style="top:527px">
    <div class="listing-photo" role="img" aria-label="Modern house lit up at night" style="background:linear-gradient(#2a3a6e,#6b6f99 50%,#c8b79a 80%,#4a4a5a)"></div>
    <h3>Nsectetur eget</h3>
    <p>Vestibulum ante ipsum primis in faucibus orci luctus et ultrices posuere. Vestibulum ante ipsum primis in faucibus orci luctus et ultrices..</p>
    <div class="price">$253,23.00</div><div class="more-btn">MORE INFO</div>
  </article>

  <h2 class="section-title" style="left:794px;top:32px">OUR TEAM</h2>
  <div class="member" style="top:81px">
    <div class="member-photo" role="img" aria-label="Team member portrait"></div>
    <h4>Name Heading</h4>
    <p>Vestibulum ante ipsum primis in faucibus orci luctus et ultrices posuere.</p>
    <div class="member-links"><span></span><span></span><span></span>
      <svg width="20" height="18" viewBox="0 0 20 18"><rect x="1" y="2" width="18" height="14" rx="2" fill="#5b5b5b"/><path d="M2 4l8 6 8-6" fill="none" stroke="#fff" stroke-width="1.5"/></svg></div>
  </div>
  <div class="member" style="top:250px">
    <div class="member-photo" role="img" aria-label="Team member portrait"></div>
    <h4>Name Heading</h4>
    <p>Vestibulum ante ipsum primis in faucibus orci luctus et ultrices posuere.</p>
    <div class="member-links"><span></span><span></span><span></span>
      <svg width="20" height="18" viewBox="0 0 20 18"><rect x="1" y="2" width="18" height="14" rx="2" fill="#5b5b5b"/><path d="M2 4l8 6 8-6" fill="none" stroke="#fff" stroke-width="1.5"/></svg></div>
  </div>
  <div class="divider"></div>

  <h2 class="section-title" style="left:794px;top:454px">BLOG POSTS</h2>
  <div class="blog-arrows">
    <span><svg width="10" height="10" viewBox="0 0 10 10"><path d="M7 1 3 5l4 4" fill="none" stroke="#fff" stroke-width="2"/></svg></span>
    <span><svg width="10" height="10" viewBox="0 0 10 10"><path d="M3 1l4 4-4 4" fill="none" stroke="#fff" stroke-width="2"/></svg></span>
  </div>
  <div class="post" style="top:512px">
    <h4>Aliquam ullamcorper tempor felis...</h4>
    <time>&#9719; Mar 05, 2016</time>
    <p>Vestibulum ante ipsum primis in faucibus orci luctus et ultrices posuere.</p>
  </div>
  <div class="post" style="top:639px">
    <h4>Aliquam ullamcorper tempor felis...</h4>
    <time>&#9719; Mar 05, 2016</time>
    <p>Vestibulum ante ipsum primis in faucibus orci luctus et ultrices posuere.</p>
  </div>
</section>

<section class="press">
  <h2>AS SEEN ON</h2>
  <div class="press-marks">
    <span style="width:114px"></span><span style="width:74px"></span><span style="width:44px;border-radius:50%;height:30px"></span><span style="width:162px"></span><span style="width:130px"></span><span style="width:175px"></span>
  </div>
</section>

<footer class="site-footer">
  <div class="abs footer-brand"><span class="brand-dot"></span><span class="brand-name">Brightmoor Crest</span></div>
  <div class="abs small-note" style="left:75px;top:100px">Copyright © 2016 All Right Reserved<br>Privacy Policy</div>

  <div class="abs footer-col" style="left:382px;top:36px">
    <h5>QUICK LINKS</h5>
    <a href="#">Home</a><a href="#">About us</a><a href="#">Services</a><a href="#">Property Search</a><a href="#">Blog</a><a href="#">Latest News</a>
  </div>
  <div class="abs footer-col" style="left:515px;top:64px">
    <a href="#">Testimonials</a><a href="#">Careers</a><a href="#">Contact us</a>
  </div>
  <div class="abs footer-col" style="left:665px;top:36px">
    <h5>CONTACT INFO</h5>
    <div>Brightmoor Crest</div><div>4120 Harlow Lane</div><div>Amarillo, TX 79101</div>
    <div style="margin-top:8px">&#9742;&nbsp; 1-800-555-0142</div>
    <div>&#9993;&nbsp; info@brightmoorcrest.example</div>
  </div>
  <div class="abs footer-col" style="left:910px;top:36px"><h5>CONNECT US</h5></div>
  <div class="abs socials"><span></span><span></span><span></span><span></span><span></span></div>
</footer>

</body>
</html>
```